Pet sitting and Dog Walking Postcard distributed to new home owners in our target market

We need a two-sided postcard (or rack card, size can be anything rack card size or smaller) that is going in a folder that will be distributed each month to new homeowners in our target area. I would like the design to be similar to our brochure which will be uploaded here for you to see. It needs much less information than the brochure.
Should include services we offer; and our 4 systems: online registration, complimentary consultation, flexible scheduling, visits with reports and photos. Should also include our contact information (website, email, phone). Photos from the brochure can be used. Tagline from the cover of the brochure can be used. Call to action should be: Register on our website today to receive a free consultation and $20 off your first booking (when requesting a service, mention the promo code: welcome20).

```html
<!DOCTYPE html>
<html lang="en">
<head>
<meta charset="utf-8">
<title>Paws Butler Pet Care – Postcard</title>
<link rel="stylesheet" href="https://fonts.googleapis.com/css2?family=Source+Sans+3:ital,wght@0,400;0,600;0,700;1,600;1,700&display=swap">
<style>
  :root {
    --purple: #5b4569;
    --green: #4fa33e;
    --green-dark: #1f6a33;
    --white: #ffffff;
    --ink: #2b2b2b;
  }
  * { margin: 0; padding: 0; box-sizing: border-box; }
  html, body { width: 1200px; height: 646px; overflow: hidden; background: var(--white); }
  body { font-family: "Source Sans 3", "Myriad Pro", sans-serif; position: relative; color: var(--purple); }

  .artwork { position: absolute; inset: 0; width: 1200px; height: 646px; }

  .headline { position: absolute; left: 57px; top: 38px; font-weight: 700; line-height: 1; letter-spacing: -0.5px; }
  .headline__top { display: block; font-size: 50px; color: var(--purple); }
  .headline__bottom { display: block; font-size: 50px; color: var(--green); margin-top: 6px; }

  .systems {
    position: absolute; left: 58px; top: 147px; list-style: none;
    display: flex; gap: 14px; font-size: 13.5px; font-weight: 700; color: var(--purple);
  }
  .systems__item { display: flex; align-items: center; gap: 5px; white-space: nowrap; }
  .systems__item::before { content: ""; width: 7px; height: 7px; border-radius: 50%; background: var(--green); }

  .services {
    position: absolute; left: 56px; top: 176px; width: 610px; height: 228px;
    border: 2px solid var(--purple); border-right: none;
    border-radius: 22px 0 0 22px; overflow: hidden;
  }
  .services__photo {
    position: absolute; left: 0; top: 0; width: 165px; height: 100%;
    background: linear-gradient(90deg, #d58a34 0%, #e9b97a 45%, #f6eadb 80%, rgba(255,255,255,0) 100%);
  }
  .services__title { position: absolute; left: 156px; top: 22px; font-size: 21px; font-weight: 700; letter-spacing: 0.4px; color: var(--purple); }
  .services__list { position: absolute; left: 156px; top: 65px; list-style: none; }
  .services__item {
    display: flex; align-items: center; gap: 8px; height: 28.5px;
    font-size: 21px; font-style: italic; font-weight: 700; color: var(--green-dark);
  }
  .services__item svg { width: 16px; height: 12px; flex: none; }

  .brand { position: absolute; left: 30px; top: 500px; width: 250px; text-align: center; color: var(--purple); font-weight: 700; font-size: 26px; line-height: 1.05; letter-spacing: 0.5px; }
  .brand__dot { width: 46px; height: 46px; border-radius: 50%; background: var(--purple); margin: 0 auto 10px; }

  .offer { position: absolute; left: 292px; top: 423px; }
  .offer__lead { font-size: 19px; font-weight: 700; line-height: 1.2; color: var(--purple); }
  .offer__lead em { font-style: normal; color: var(--green); }
  .offer__note { font-size: 16px; color: var(--ink); margin-top: 12px; }

  .promo {
    position: absolute; left: 292px; top: 523px; width: 552px; height: 49px;
    background: var(--green); clip-path: polygon(0 0, 87% 0, 100% 100%, 0 100%);
    color: var(--white); font-size: 31px; font-weight: 700; line-height: 49px; padding-left: 22px;
  }

  .contact { position: absolute; left: 292px; top: 592px; display: flex; align-items: center; gap: 16px; font-size: 20px; font-weight: 700; color: var(--purple); }
  .contact__item { display: flex; align-items: center; gap: 6px; white-space: nowrap; }
  .contact__item svg { width: 18px; height: 18px; flex: none; }
</style>
</head>
<body>

<svg class="artwork" viewBox="0 0 1200 646">
  <defs>
    <linearGradient id="hero-tone" gradientUnits="userSpaceOnUse" x1="700" y1="0" x2="1200" y2="550">
      <stop offset="0" stop-color="#f6efe6"/>
      <stop offset="0.55" stop-color="#e6cdb3"/>
      <stop offset="1" stop-color="#6f7590"/>
    </linearGradient>
    <linearGradient id="cat-tone" x1="0" y1="0" x2="1" y2="1">
      <stop offset="0" stop-color="#c9b7a6"/>
      <stop offset="1" stop-color="#7d7470"/>
    </linearGradient>
    <linearGradient id="food-tone" x1="0" y1="0" x2="0" y2="1">
      <stop offset="0" stop-color="#f1ece4"/>
      <stop offset="0.55" stop-color="#d9ae78"/>
      <stop offset="1" stop-color="#8b5a2b"/>
    </linearGradient>
  </defs>

  <g role="img" aria-label="Photo of a smiling woman on a sofa hugging a brown and white spaniel">
    <circle cx="1000" cy="235" r="315" fill="url(#hero-tone)"/>
    <rect x="1000" y="0" width="200" height="240" fill="url(#hero-tone)"/>
  </g>
  <circle cx="1000" cy="235" r="315" fill="none" stroke="var(--purple)" stroke-width="7"/>
  <path d="M 797 508 A 340 340 0 0 0 1200 510" fill="none" stroke="var(--green)" stroke-width="6"/>

  <g role="img" aria-label="Photo of a grey tabby cat being petted">
    <circle cx="708" cy="264" r="118" fill="url(#cat-tone)" stroke="var(--white)" stroke-width="9"/>
  </g>

  <g role="img" aria-label="Photo of a dog eating kibble from a bowl">
    <circle cx="1072" cy="516" r="90" fill="url(#food-tone)" stroke="var(--white)" stroke-width="9"/>
  </g>
</svg>

<h1 class="headline">
  <span class="headline__top">Prioritize Yourself.</span>
  <span class="headline__bottom">We’ll Focus on Your Pets.</span>
</h1>

<ul class="systems">
  <li class="systems__item">Online Registration</li>
  <li class="systems__item">Complimentary Consultation</li>
  <li class="systems__item">Flexible Scheduling</li>
  <li class="systems__item">Visits with Reports &amp; Photos</li>
</ul>

<section class="services">
  <div class="services__photo" role="img" aria-label="Photo of a yellow labrador holding a blue leash in its mouth by a front door"></div>
  <h2 class="services__title">PROFESSIONAL PET CARE SERVICES</h2>
  <ul class="services__list">
    <li class="services__item"><svg viewBox="0 0 16 12"><path d="M1 5 L6 10 L15 1" fill="none" stroke="var(--purple)" stroke-width="3"/></svg>Day care and Overnight Boarding</li>
    <li class="services__item"><svg viewBox="0 0 16 12"><path d="M1 5 L6 10 L15 1" fill="none" stroke="var(--purple)" stroke-width="3"/></svg>Sleeplovers</li>
    <li class="services__item"><svg viewBox="0 0 16 12"><path d="M1 5 L6 10 L15 1" fill="none" stroke="var(--purple)" stroke-width="3"/></svg>Dog Walking</li>
    <li class="services__item"><svg viewBox="0 0 16 12"><path d="M1 5 L6 10 L15 1" fill="none" stroke="var(--purple)" stroke-width="3"/></svg>Pet Sitting</li>
    <li class="services__item"><svg viewBox="0 0 16 12"><path d="M1 5 L6 10 L15 1" fill="none" stroke="var(--purple)" stroke-width="3"/></svg>Cat Sitting/Small Pet Sitting</li>
  </ul>
</section>

<div class="brand">
  <div class="brand__dot"></div>
  PAWS BUTLER<br>PET CARE
</div>

<div class="offer">
  <p class="offer__lead">Register on our website today to receive a<br><em>free consultation</em> and <em>$20 off</em> your first booking</p>
  <p class="offer__note">when requesting a service, mention the</p>
</div>

<div class="promo">Promo code : welcome20</div>

<div class="contact">
  <span class="contact__item">
    <svg viewBox="0 0 24 24"><circle cx="12" cy="12" r="10" fill="none" stroke="var(--green)" stroke-width="2"/><path d="M2 12h20M12 2c-4 4-4 16 0 20M12 2c4 4 4 16 0 20" fill="none" stroke="var(--green)" stroke-width="1.6"/></svg>
    www.pawsbutlerpets.com
  </span>
  <span class="contact__item">
    <svg viewBox="0 0 24 24"><path d="M6.6 10.8a15 15 0 0 0 6.6 6.6l2.2-2.2a1 1 0 0 1 1-.25 11.4 11.4 0 0 0 3.6.6 1 1 0 0 1 1 1V20a1 1 0 0 1-1 1A17 17 0 0 1 3 4a1 1 0 0 1 1-1h3.5a1 1 0 0 1 1 1c0 1.25.2 2.45.6 3.6a1 1 0 0 1-.25 1z" fill="var(--green)"/></svg>
    555-010-BARK
  </span>
  <span class="contact__item">
    <svg viewBox="0 0 24 24"><rect x="2" y="5" width="20" height="14" rx="2" fill="none" stroke="var(--green)" stroke-width="2"/><path d="M3 6l9 7 9-7" fill="none" stroke="var(--green)" stroke-width="2"/></svg>
    hello@pawsbutlerpets.com
  </span>
</div>

</body>
</html>
```